lunavo GmbH needs great looking businesscards to leave an impression

Dear Designers,

Our company lunavo GmbH based in switzerland needs to have impressive businesscards. We produce and sell high quality bleaching products for the upper market.
We'd like to have a minimalistic but still meaningful design. You'll fine our company logo attached and some of our packaging designs. Our company slogan is "discover your smile". If you need additional information feel free to contact us.
Kind Regards Milo

Dear Designers, This is a business card design contest! I try to call the support to fix that. Kind Regards Milo

```html
<!DOCTYPE html>
<html lang="de">
<head>
<meta charset="utf-8">
<title>lunavo GmbH – Visitenkarte</title>
<link rel="stylesheet" href="https://fonts.googleapis.com/css2?family=Lato:wght@300;400&display=swap">
<style>
  :root {
    --teal: #1c5d6b;
    --teal-deep: #164b57;
    --paper: #f7f7f5;
    --ink: #5a5a5a;
    --backdrop: #e6e6e3;
  }
  html, body {
    margin: 0;
    width: 1200px;
    height: 1023px;
    overflow: hidden;
    background: var(--backdrop);
  }
  .canvas {
    position: relative;
    width: 1200px;
    height: 1023px;
  }
  .card {
    position: absolute;
    top: 337px;
    width: 540px;
    height: 349px;
    border-radius: 4px;
    overflow: hidden;
    box-shadow: 0 6px 18px rgba(0,0,0,.18);
  }
  .card--front { left: 40px; background: var(--paper); }
  .card--back { left: 620px; background: var(--teal); }

  .front-art { position: absolute; inset: 0; }

  .details {
    position: absolute;
    left: 36px;
    top: 40px;
    font-family: "Lato", sans-serif;
    font-weight: 300;
    color: var(--ink);
    font-size: 17px;
    line-height: 22px;
  }
  .details p { margin: 0; }
  .contact { margin-top: 20px; }
  .contact-line { display: flex; align-items: center; gap: 8px; }
  .contact-line svg { width: 16px; height: 16px; }

  .wordmark {
    position: absolute;
    left: 36px;
    bottom: 44px;
    display: flex;
    align-items: center;
    gap: 10px;
    font-family: "Lato", sans-serif;
    font-weight: 300;
    font-size: 30px;
    color: var(--teal);
  }
  .wordmark-dot {
    width: 26px;
    height: 26px;
    border-radius: 50%;
    background: var(--teal);
  }

  .back-pattern {
    position: absolute;
    inset: 0;
    background: linear-gradient(135deg, var(--teal) 0%, var(--teal-deep) 100%);
  }
</style>
</head>
<body>
<div class="canvas">

  <section class="card card--front">
    <svg class="front-art" viewBox="0 0 540 349" aria-hidden="true">
      <circle cx="470" cy="40" r="250" fill="var(--teal)"/>
      <rect x="0" y="321" width="540" height="28" fill="var(--teal)"/>
    </svg>

    <div class="details">
      <p>lunavo GmbH</p>
      <p>Mister</p>
      <p>Jonas Berner</p>
      <p>Lindenhofweg 14</p>
      <p>8004 Zürich</p>
      <div class="contact">
        <p class="contact-line">0041 79 456 78 90
          <svg viewBox="0 0 16 16"><rect x="4" y="1" width="8" height="14" rx="1.5" fill="none" stroke="var(--teal)" stroke-width="1.5"/><circle cx="8" cy="12.5" r="0.9" fill="var(--teal)"/></svg>
        </p>
        <p class="contact-line">jonas.berner@mailbox.ch
          <svg viewBox="0 0 16 16"><rect x="1" y="3" width="14" height="10" fill="var(--teal)"/><path d="M1 3 L8 9 L15 3" fill="none" stroke="#fff" stroke-width="1"/></svg>
        </p>
      </div>
    </div>

    <div class="wordmark">
      <span>lunavo</span>
      <span class="wordmark-dot"></span>
    </div>
  </section>

  <section class="card card--back">
    <div class="back-pattern" role="img" aria-label="Teal decorative pattern of flowers and diamonds"></div>
  </section>

</div>
</body>
</html>
```